Trifold Brochure Design Project

We need a trifold brochure design for a company/product called VitaLume. We provide full-body MRI screening, along with blood chemistry and DNA analysis, followed by a consultation with the MD in a comfortable outpatient setting.
The facility is located in Fort Lauderdale, Florida.
The concept is that people usually don't know about many diseases until they are far advanced and more difficult to treat. We offer early detection which leads to early treatment and better outcomes.
The concept should blend an emotional construct (do it for yourself or someone you love, the best gift is health, live longer to love longer, etc) with science to legitimize the service. (MRI, Blood Chemistry, DNA analysis and an MD to interpret)

Target Market(s)

Baby boomers and active middle-age men and women

Industry/Entity Type

It Company

Requirements
Must have
• Attractive middle age people enjoying life because they know they are healthy.
Services are provided 7-days a week in a comfortable outpatient setting. Everything is totally confidential.
VitaLume is a division of Crestline Scan & Imaging Centers
Nice to have
• Some clinical imagery such as the doctor, the MRI machine or inferences that this is a clinical-based solution.
Extremely experienced, qualified and licensed Doctors and Technologists are involved.

```html
<!DOCTYPE html>
<html lang="en">
<head>
<meta charset="utf-8">
<title>VitaLume Trifold Brochure</title>
<link href="https://fonts.googleapis.com/css2?family=Oswald:wght@400;500&family=Arimo:wght@400&display=swap" rel="stylesheet">
<style>
  :root {
    --page-bg: #e9edf1;
    --teal: #6aafb9;
    --navy: #1d5b93;
    --navy-deep: #184e82;
    --sky: #2f8ce0;
    --sky-light: #7cc0f3;
    --white: #ffffff;
    --logo-navy: #1b4f8c;
    --logo-teal: #77b4bd;
  }
  * { margin: 0; padding: 0; box-sizing: border-box; }
  html, body { width: 1200px; height: 1062px; overflow: hidden; }
  body { background: var(--page-bg); position: relative; font-family: "Arimo", Arial, sans-serif; }

  .panel {
    position: absolute; top: 80px; width: 420px; height: 900px; overflow: hidden;
    box-shadow: 0 10px 30px rgba(0,0,0,0.25);
  }

  /* Back panel */
  .panel--back { left: 150px; background: var(--teal); color: var(--white); }
  .back-shapes { position: absolute; inset: 0; }
  .back-brand {
    position: absolute; left: 82px; top: 60px;
    font-family: "Arimo", Arial, sans-serif; font-size: 44px; color: var(--white);
  }
  .back-brand-dot {
    position: absolute; left: 205px; top: 40px; width: 22px; height: 22px;
    border-radius: 50%; background: var(--white);
  }
  .back-rule { position: absolute; left: 40px; right: 26px; top: 152px; height: 2px; background: rgba(255,255,255,0.85); }
  .back-headline {
    position: absolute; left: 62px; right: 20px; top: 180px;
    font-family: "Oswald", sans-serif; font-weight: 400; font-size: 35px; line-height: 38px;
  }
  .back-body {
    position: absolute; left: 62px; right: 20px; top: 362px;
    font-size: 24px; line-height: 38px;
  }
  .back-address { position: absolute; left: 60px; bottom: 80px; font-size: 13px; line-height: 18px; }
  .back-address-label { font-family: "Oswald", sans-serif; font-weight: 500; font-size: 13px; margin-bottom: 6px; }
  .back-web {
    position: absolute; left: 60px; bottom: 28px;
    font-family: "Oswald", sans-serif; font-size: 19px; letter-spacing: 4px;
  }

  /* Front panel */
  .panel--front { left: 630px; background: linear-gradient(180deg, #3d94e3 0%, var(--sky) 40%, #4aa0e8 70%, #a8d4f6 100%); color: var(--white); }
  .front-logo-bars { position: absolute; left: 168px; top: 42px; width: 9px; height: 102px; }
  .front-logo-bar-top { height: 58px; background: var(--logo-navy); }
  .front-logo-bar-bottom { height: 44px; background: var(--logo-teal); }
  .front-logo-box {
    position: absolute; left: 177px; top: 42px; width: 243px; height: 102px; background: var(--white);
    display: flex; align-items: center; justify-content: center; gap: 10px;
  }
  .front-brand { font-family: "Arimo", Arial, sans-serif; font-size: 36px; color: var(--logo-navy); }
  .front-brand-dot { width: 14px; height: 14px; border-radius: 50%; background: var(--logo-navy); }
  .front-headline {
    position: absolute; left: 68px; right: 20px; top: 180px;
    font-family: "Oswald", sans-serif; font-weight: 400; font-size: 38px; line-height: 44px;
    text-shadow: 0 2px 6px rgba(0,0,0,0.3);
  }
  .front-intro { position: absolute; left: 68px; right: 20px; top: 282px; font-size: 17px; line-height: 24px; }
  .front-photo-scanner {
    position: absolute; left: 0; right: 0; top: 370px; height: 330px;
    background: radial-gradient(ellipse at 70% 45%, #f1f5f8 0%, #cfdbe6 35%, #5fa6e6 75%, rgba(47,140,224,0) 100%);
  }
  .front-photo-people {
    position: absolute; left: 20px; right: 0; top: 680px; height: 220px;
    background: radial-gradient(ellipse at 55% 60%, #f4efe8 0%, #dcc2a8 40%, #b6cde3 80%, rgba(168,212,246,0.6) 100%);
  }
</style>
</head>
<body>

<section class="panel panel--back" aria-label="Brochure back panel">
  <svg class="back-shapes" width="420" height="900" viewBox="0 0 420 900" aria-hidden="true">
    <polygon points="0,650 420,900 0,900" fill="var(--navy)"/>
    <polygon points="0,650 420,560 420,900" fill="var(--navy-deep)"/>
    <polygon points="420,700 420,900 290,900" fill="var(--teal)" opacity="0.55"/>
  </svg>
  <div class="back-brand-dot" aria-hidden="true"></div>
  <div class="back-brand">VitaLume</div>
  <div class="back-rule"></div>
  <h2 class="back-headline">Services are provided 7-days a week in a comfortable outpatient setting.</h2>
  <p class="back-body">Everything is totally confidential.<br>VitaLume is a division of Crestline Scan &amp; Imaging Centers</p>
  <div class="back-address">
    <div class="back-address-label">ADDRESS</div>
    dolor sit amet, consectetuer<br>adipiscing elit, sed diam<br>nonummy nibh euismod Lorem<br>ipsum dolor sit amet, consectet
  </div>
  <div class="back-web">www.yourwebsite.com</div>
</section>

<section class="panel panel--front" aria-label="Brochure front panel">
  <div class="front-logo-bars" aria-hidden="true">
    <div class="front-logo-bar-top"></div>
    <div class="front-logo-bar-bottom"></div>
  </div>
  <div class="front-logo-box">
    <span class="front-brand-dot" aria-hidden="true"></span>
    <span class="front-brand">VitaLume</span>
  </div>
  <h1 class="front-headline">Headline goes<br>here for the brochure</h1>
  <p class="front-intro">Lorem ipsum dolor sit amet, consectetuer adipiscing elit, sed diam nonummy nibh euismod</p>
  <div class="front-photo-scanner" role="img" aria-label="Photo of a modern MRI scanner with its patient table"></div>
  <div class="front-photo-people" role="img" aria-label="Photo of a smiling middle-aged couple in white bathrobes"></div>
</section>

</body>
</html>
```